Looking for a quillet ebook cover. Must meet all quillet open printing specifics. *

I need a book cover for my romance novel. The title is "Rain, Forgotten". I would like this in typographic and an illustration below ( as a reference you can see Far Shores by Doreen Plaskett). The author name is T L Venn. The story is set in England in the countryside, during fall and winter. It is a love/coming of age novel about a young couple. The girl is a writer, the boy is overcoming illness. The ending is tragic. The tone of the cover should convey an emotional read about true love and separation. It is a book for readers who enjoy novels by Bibi Trallow, Philippa Dunmore, Doreen Plaskett.

Target Market(s)

Women in their 20s and 30s who enjoy romance.

Industry/Entity Type

Publishing

Font styles to use
Sans Serif

Requirements
Must have
• You can stress the title more than the author name on the cover.
Should not have
• No photographs.

```html
<!DOCTYPE html>
<html lang="en">
<head>
<meta charset="utf-8">
<title>Rain, Forgotten — T L Venn</title>
<link rel="stylesheet" href="https://fonts.googleapis.com/css2?family=Cinzel:wght@400;500&display=swap">
<style>
  :root {
    --backdrop: #ececec;
    --crimson: #b01c30;
    --magenta: #d42a7a;
    --azure: #0a78c2;
    --teal: #13bf9c;
    --saffron: #f5b623;
    --ink-blue: #1a4fa0;
    --heart-tint: #d9567a;
    --title-white: #ffffff;
    --author-gold: #ecc58d;
  }
  html, body {
    margin: 0;
    width: 960px;
    height: 1200px;
    overflow: hidden;
    background: var(--backdrop);
  }
  .book-cover {
    position: absolute;
    left: 141px;
    top: 40px;
    width: 677px;
    height: 1120px;
    display: block;
    box-shadow: 0 6px 24px rgba(0,0,0,0.18);
  }
  .block-crimson { fill: var(--crimson); }
  .block-magenta { fill: var(--magenta); }
  .block-azure { fill: var(--azure); }
  .block-teal { fill: var(--teal); }
  .block-saffron { fill: var(--saffron); }
  .title-swash { fill: var(--ink-blue); }
  .heart-mark { fill: var(--heart-tint); opacity: 0.55; }
  .cover-title {
    font-family: "Cinzel", "Times New Roman", serif;
    fill: var(--title-white);
    text-anchor: middle;
  }
  .cover-title .line-main { font-size: 128px; font-weight: 400; }
  .cover-title .line-sub { font-size: 66px; font-weight: 500; }
  .cover-author {
    font-family: "Cinzel", "Times New Roman", serif;
    font-size: 30px;
    letter-spacing: 2px;
    fill: var(--author-gold);
    text-anchor: middle;
  }
</style>
</head>
<body>
  <svg class="book-cover" viewBox="0 0 677 1120" xmlns="http://www.w3.org/2000/svg">
    <g class="colour-blocks">
      <rect class="block-crimson" x="0" y="0" width="377" height="143"/>
      <rect class="block-magenta" x="0" y="143" width="377" height="977"/>
      <rect class="block-azure" x="377" y="0" width="300" height="323"/>
      <rect class="block-teal" x="377" y="323" width="153" height="274"/>
      <rect class="block-saffron" x="530" y="323" width="147" height="274"/>
      <rect class="block-crimson" x="377" y="597" width="300" height="523"/>
    </g>

    <rect class="heart-mark" x="390" y="720" width="180" height="227" rx="60"
          role="img" aria-label="Loose brush-painted heart in soft pink"/>

    <rect class="title-swash" x="91" y="188" width="540" height="240" rx="40"
          role="img" aria-label="Deep blue painted brush stroke behind the title"/>

    <text class="cover-title">
      <tspan class="line-main" x="324" y="318">RAIN,</tspan>
      <tspan class="line-sub" x="360" y="392">FORGOTTEN</tspan>
    </text>

    <text class="cover-author" x="511" y="1007">T L VENN</text>
  </svg>
</body>
</html>
```